i need a business card for a plumbing company in california

we are a drain cleaning , maintenance plumbing company who is starting new marketing campaign for a tatrench-less pipe installation department .

the professional who appreciates time and quality workmanship.

Plumbing

0655a3
ec1f27

• the second logo needs to be included
• a focus on the services offered
• any underlined words on the brief

```html
<!DOCTYPE html>
<html lang="en">
<head>
<meta charset="utf-8">
<title>Clearflow Plumbing – Business Card</title>
<link rel="stylesheet" href="https://fonts.googleapis.com/css2?family=Roboto:wght@500;700;900&family=Tinos:wght@400;700&display=swap">
<style>
  :root{
    --brand-blue:#0655a3;
    --brand-blue-deep:#0a3f80;
    --brand-red:#ec1f27;
    --logo-grey:#7a7a72;
    --card-white:#ffffff;
    --card-shade:#eeeeee;
    --stage:#2b2b2b;
    --ink-light:#ffffff;
  }
  *{margin:0;padding:0;box-sizing:border-box}
  html,body{width:1200px;height:997px;overflow:hidden}
  body{background:var(--stage);position:relative;font-family:"Roboto",Arial,sans-serif}
  .card{
    position:absolute;top:344px;width:540px;height:310px;border-radius:18px;overflow:hidden;
    background:linear-gradient(160deg,var(--card-white) 55%,var(--card-shade));
    box-shadow:0 18px 40px rgba(0,0,0,.55);
  }
  .card--services{left:40px}
  .card--contact{left:620px}
  .card__art{position:absolute;inset:0;width:100%;height:100%}
  .brand{
    position:absolute;top:24px;right:34px;display:flex;align-items:center;gap:12px;
  }
  .brand__name{
    font-weight:900;font-size:30px;line-height:.95;color:var(--logo-grey);text-align:right;letter-spacing:.5px;
  }
  .brand__dot{width:34px;height:34px;border-radius:50%;background:var(--brand-red)}
  .service{
    position:absolute;font-weight:700;font-size:11px;letter-spacing:.6px;text-transform:uppercase;white-space:nowrap;line-height:13px;
  }
  .service--red{color:var(--brand-red)}
  .service--blue{color:var(--brand-blue)}
  .services-tag{
    position:absolute;left:22px;top:272px;width:170px;height:28px;border-radius:14px;
    background:var(--brand-blue);color:var(--ink-light);font-weight:700;font-size:12.5px;letter-spacing:1.2px;
    display:flex;align-items:center;justify-content:center;
  }
  .contact{position:absolute;left:30px;top:196px;color:var(--ink-light)}
  .contact__name{font-weight:900;font-size:19px;letter-spacing:1px;color:var(--brand-red);text-transform:uppercase}
  .contact__role{font-weight:500;font-size:12px;margin-bottom:7px}
  .contact__line{display:flex;align-items:center;gap:9px;font-family:"Tinos",Georgia,serif;font-size:14px;line-height:19px}
  .contact__icon{width:11px;height:11px;flex:none}
</style>
</head>
<body>

<section class="card card--services" aria-label="Card back: services">
  <svg class="card__art" viewBox="0 0 540 310" aria-hidden="true">
    <path d="M0,262 C150,190 300,190 540,118" fill="none" stroke="var(--brand-red)" stroke-width="9"/>
    <path d="M0,274 C150,202 300,202 540,130" fill="none" stroke="var(--brand-blue)" stroke-width="9"/>
    <path d="M0,294 C80,298 160,304 230,310 L0,310 Z" fill="var(--brand-blue)"/>
    <g fill="var(--brand-blue)" stroke="var(--card-white)" stroke-width="3">
      <circle cx="138" cy="219" r="19"/>
      <circle cx="289" cy="185" r="19"/>
      <circle cx="438" cy="152" r="19"/>
    </g>
    <g fill="var(--ink-light)" font-family="Tinos, Georgia, serif" font-size="24" font-weight="700" text-anchor="middle">
      <text x="138" y="227">1</text>
      <text x="289" y="193">2</text>
      <text x="438" y="160">3</text>
    </g>
  </svg>

  <div class="brand">
    <div class="brand__name">Clearflow<br>Plumbing</div>
    <div class="brand__dot"></div>
  </div>

  <p class="service service--red" style="left:100px;top:250px">Sewer Drain Cleaning</p>
  <p class="service service--blue" style="left:246px;top:214px">Maintenance</p>
  <p class="service service--red" style="left:345px;top:182px">Trenchless Pipe Installs</p>

  <div class="services-tag">OUR SERVICES</div>
</section>

<section class="card card--contact" aria-label="Card front: contact">
  <svg class="card__art" viewBox="0 0 540 310" aria-hidden="true">
    <path d="M0,176 C150,150 250,200 380,196 C450,194 500,176 540,160 L540,310 L0,310 Z" fill="var(--brand-red)"/>
    <path d="M0,192 C150,166 250,216 380,212 C450,210 500,192 540,176 L540,310 L0,310 Z" fill="var(--brand-blue)"/>
    <path d="M0,192 C150,166 250,216 380,212 C450,210 500,192 540,176 L540,310 L0,310 Z" fill="var(--brand-blue-deep)" opacity=".35"/>
  </svg>

  <div class="brand" style="top:58px">
    <div class="brand__name">Clearflow<br>Plumbing</div>
    <div class="brand__dot"></div>
  </div>

  <div class="contact">
    <p class="contact__name">Marco Delgado</p>
    <p class="contact__role">Director</p>
    <p class="contact__line">
      <svg class="contact__icon" viewBox="0 0 12 12"><rect x="3" y="0.5" width="6" height="11" rx="1.2" fill="none" stroke="#fff" stroke-width="1.3"/><circle cx="6" cy="9.5" r=".8" fill="#fff"/></svg>
      0400-555-019
    </p>
    <p class="contact__line">
      <svg class="contact__icon" viewBox="0 0 12 12"><rect x="0.5" y="2.5" width="11" height="7" fill="#fff"/><path d="M0.5,2.5 L6,6.5 L11.5,2.5" fill="none" stroke="#0655a3" stroke-width="1"/></svg>
      m.delgado@clearflowplumbing.com
    </p>
    <p class="contact__line">
      <svg class="contact__icon" viewBox="0 0 12 12"><g fill="none" stroke="#fff" stroke-width="1.4"><rect x="0.8" y="5" width="6" height="3.5" rx="1.7" transform="rotate(-45 3.8 6.7)"/><rect x="5.2" y="3.5" width="6" height="3.5" rx="1.7" transform="rotate(-45 8.2 5.2)"/></g></svg>
      www.clearflowplumbing.com
    </p>
  </div>
</section>

</body>
</html>
```